New Website Footer for a Supercar dealership.

I'm looking to get a newly designed footer created for our website www.velmorcarhouse.com - one version for Desktop and 1 trimmed down version for mobile. We have one in place at the moment but I want to start it from scratch and create something far better. I know what I want to include and I have a rough design to work from which I have included in the uploaded files and I am just looking for someone to give it a high end luxury design.

If you see the sketch I've done - it must include the following links
- CURRENT STOCK
- SELL YOUR CAR
- PREVIOUSLY SOLD
Ideally use the same font that we have on our website in the top navigation

Secondary Links (in lower case)
- Delivery & Shipping
- Privacy Policy
- Modern Slavery Statement
- Luxury Cars
- Contact Us

I want also want to include
- Opening Hours
- Widget for Ratewell
- Widget for Praisly Reviews
- 4 images for awards we have won (I have included in uploaded files)
- Mailing List Sign Up
- Our company logo and address
- Quorin Finance logo (partner)
- Cookie Policy and Site Map links.
- Social Media icons

You do not have to stick to the layout of my design - feel free to change it about. I am open to colour but it needs to stay subtle and ideally working within Greyscale.

I am looking to have a black background but has a textured element to it. I was thinking along the lines of carbon fibre effect or even better would be a "Forged carbon fibre" effect in the background - I have included a screenshot of what ford carbon fibre looks like.

Target Market(s)

Luxury high end buyers

Industry/Entity Type

Automotive

Number of Pages Required

1 page

Font styles to use
Serif
Sans Serif

Colors

Designer to choose only greyscale colors for use in the design.

Requirements
Must have
• 1 Version for Desktop
1 Version for Mobile

```html
<!DOCTYPE html>
<html lang="en">
<head>
<meta charset="utf-8">
<title>Velmor Car House – Footer</title>
<link rel="stylesheet" href="https://fonts.googleapis.com/css2?family=Montserrat:wght@400;500;600;700&display=swap">
<style>
  :root {
    --bg-deep: #0a0a0a;
    --bg-mid: #1b1b1b;
    --ink: #f2f2f2;
    --ink-soft: #cfcfcf;
    --rule: #6a6a6a;
    --panel: #d9d9d9;
    --panel-ink: #2a2a2a;
    --field: #f4f4f4;
    --button: #111111;
    --badge-a: #3a3a3a;
    --badge-b: #8c8c8c;
    --star: #bdbdbd;
    --scratch: #ffffff;
    --tile: #ffffff;
    --tile-ink: #111111;
  }
  * { box-sizing: border-box; margin: 0; padding: 0; }
  html, body { width: 1200px; height: 3800px; overflow: hidden; }
  body {
    position: relative;
    font-family: "Montserrat", sans-serif;
    color: var(--ink);
    background: var(--bg-deep);
  }
  .texture {
    position: absolute; inset: 0;
    background:
      repeating-linear-gradient(90deg, rgba(255,255,255,0.018) 0 1px, transparent 1px 5px),
      repeating-linear-gradient(0deg, rgba(0,0,0,0.25) 0 1px, transparent 1px 4px),
      radial-gradient(ellipse at 30% 20%, #272727 0%, transparent 55%),
      radial-gradient(ellipse at 75% 65%, #232323 0%, transparent 50%),
      radial-gradient(ellipse at 50% 95%, #202020 0%, transparent 45%),
      linear-gradient(160deg, var(--bg-mid), var(--bg-deep) 60%, #151515);
  }
  .scratches { position: absolute; inset: 0; }
  .scratches line { stroke: var(--scratch); stroke-linecap: round; }
  .abs { position: absolute; }
  .center { left: 0; width: 1200px; text-align: center; }
  .rule { position: absolute; left: 60px; width: 1080px; height: 2px; background: var(--rule); }
  .nav-link { font-size: 28px; font-weight: 500; letter-spacing: 1px; }
  .heading { font-size: 36px; font-weight: 600; }
  .heading--caps { text-transform: uppercase; letter-spacing: 1px; }
  .hours-row { font-size: 27px; display: flex; height: 56px; }
  .hours-day { width: 192px; }
  .sub-link { font-size: 28px; left: 352px; }
  .badge { position: absolute; border-radius: 4px; }
  .rating { position: absolute; left: 352px; font-size: 24px; }
  .stars { position: absolute; left: 500px; }
  .rating-name { font-size: 26px; font-weight: 600; }
  .mailing {
    position: absolute; left: 296px; top: 2060px; width: 576px; height: 248px;
    background: var(--panel); color: var(--panel-ink); padding: 22px 22px;
  }
  .mailing-title { font-size: 28px; font-weight: 700; text-transform: uppercase; letter-spacing: 0.5px; white-space: nowrap; }
  .mailing-text { font-size: 21px; line-height: 30px; margin-top: 10px; }
  .mailing-form { display: flex; gap: 12px; margin-top: 22px; }
  .mailing-input { width: 316px; height: 60px; background: var(--field); border: 1px solid #999; font-size: 22px; color: #777; padding: 16px 14px; }
  .mailing-button { width: 206px; height: 60px; background: var(--button); color: var(--ink); font-size: 22px; font-weight: 700; letter-spacing: 1px; text-align: center; line-height: 60px; }
  .brand-name { font-size: 30px; font-weight: 500; letter-spacing: 2px; text-transform: uppercase; }
  .address { position: absolute; left: 572px; font-size: 26px; line-height: 48px; }
  .partner { position: absolute; top: 2978px; font-size: 40px; font-weight: 500; }
  .social-label { position: absolute; top: 3326px; font-size: 34px; transform: translateX(-50%); white-space: nowrap; }
  .social-tile {
    position: absolute; top: 3400px; width: 72px; height: 72px; background: var(--tile);
    transform: translateX(-50%); color: var(--tile-ink);
    font-size: 24px; font-weight: 700; text-align: center; line-height: 72px;
  }
  .legal { font-size: 24px; }
</style>
</head>
<body>
  <div class="texture" role="img" aria-label="Scratched black carbon texture background"></div>
  <svg class="scratches" width="1200" height="3800" viewBox="0 0 1200 3800" aria-hidden="true">
    <g stroke-width="1" opacity="0.09">
      <line x1="40" y1="120" x2="320" y2="420"/>
      <line x1="900" y1="60" x2="1180" y2="380"/>
      <line x1="760" y1="480" x2="1100" y2="760"/>
      <line x1="20" y1="700" x2="260" y2="1020"/>
      <line x1="980" y1="900" x2="1190" y2="1260"/>
      <line x1="60" y1="1300" x2="300" y2="1500"/>
      <line x1="820" y1="1420" x2="1160" y2="1700"/>
      <line x1="30" y1="1820" x2="220" y2="2160"/>
      <line x1="940" y1="1900" x2="1190" y2="2220"/>
      <line x1="100" y1="2400" x2="360" y2="2700"/>
      <line x1="860" y1="2460" x2="1150" y2="2780"/>
      <line x1="20" y1="2900" x2="240" y2="3180"/>
      <line x1="960" y1="3000" x2="1190" y2="3320"/>
      <line x1="80" y1="3500" x2="340" y2="3760"/>
      <line x1="840" y1="3560" x2="1120" y2="3790"/>
    </g>
    <g stroke-width="0.8" opacity="0.06">
      <line x1="200" y1="40" x2="120" y2="380"/>
      <line x1="1100" y1="500" x2="980" y2="640"/>
      <line x1="300" y1="860" x2="80" y2="1100"/>
      <line x1="1160" y1="1100" x2="1000" y2="1380"/>
      <line x1="260" y1="1600" x2="40" y2="1760"/>
      <line x1="1180" y1="2000" x2="1060" y2="2340"/>
      <line x1="240" y1="2200" x2="60" y2="2520"/>
      <line x1="1140" y1="2600" x2="980" y2="2900"/>
      <line x1="280" y1="3100" x2="40" y2="3440"/>
      <line x1="1180" y1="3300" x2="1040" y2="3600"/>
      <line x1="500" y1="20" x2="700" y2="140"/>
      <line x1="480" y1="3700" x2="720" y2="3790"/>
    </g>
  </svg>

  <nav>
    <div class="abs center nav-link" style="top:144px">CURRENT STOCK</div>
    <div class="abs center nav-link" style="top:204px">SELL YOUR CAR</div>
    <div class="abs center nav-link" style="top:264px">PREVIOUSLY SOLD</div>
  </nav>
  <div class="rule" style="top:368px"></div>

  <section>
    <h2 class="abs center heading" style="top:430px">Opening Hours</h2>
    <div class="abs" style="left:352px; top:532px">
      <div class="hours-row"><span class="hours-day">Monday :</span><span>8.30am - 6.00pm</span></div>
      <div class="hours-row"><span class="hours-day">Tuesday :</span><span>8.30am - 6.00pm</span></div>
      <div class="hours-row"><span class="hours-day">Wednesday :</span><span>8.30am - 6.00pm</span></div>
      <div class="hours-row"><span class="hours-day">Thursday :</span><span>8.30am - 6.00pm</span></div>
      <div class="hours-row"><span class="hours-day">Friday :</span><span>8.30am - 6.00pm</span></div>
      <div class="hours-row"><span class="hours-day">Saturday :</span><span>8.30am - 6.00pm</span></div>
      <div class="hours-row"><span class="hours-day">Sunday :</span><span>By Appointment Only</span></div>
    </div>
  </section>
  <div class="rule" style="top:972px"></div>

  <section>
    <div class="abs sub-link" style="top:1044px">Delivery &amp; Shipping</div>
    <div class="abs sub-link" style="top:1100px">Privacy Policy</div>
    <div class="abs sub-link" style="top:1156px">Modern Slavery Statement</div>
    <div class="abs sub-link" style="top:1212px">Luxury Cars</div>
    <div class="abs sub-link" style="top:1268px">Contact Us</div>
  </section>
  <div class="rule" style="top:1368px"></div>

  <section>
    <div class="badge" style="left:352px; top:1436px; width:140px; height:116px; background:var(--badge-a)" role="img" aria-label="Award badge"></div>
    <div class="badge" style="left:518px; top:1436px; width:204px; height:116px; background:var(--badge-b)" role="img" aria-label="Award badge"></div>
    <div class="badge" style="left:352px; top:1566px; width:140px; height:140px; background:var(--badge-a)" role="img" aria-label="Award badge"></div>
    <div class="badge" style="left:518px; top:1566px; width:204px; height:140px; background:var(--badge-b)" role="img" aria-label="Award badge"></div>

    <div class="rating" style="top:1740px">Excellent</div>
    <svg class="stars" style="top:1734px" width="216" height="42" viewBox="0 0 216 42" aria-hidden="true">
      <g fill="var(--star)">
        <path id="star" d="M21 3l5.3 11.6 12.7 1.3-9.5 8.5 2.7 12.5L21 30.5 9.8 36.9l2.7-12.5L3 15.9l12.7-1.3z"/>
        <use href="#star" x="43"/><use href="#star" x="86"/><use href="#star" x="129"/><use href="#star" x="172"/>
      </g>
    </svg>
    <div class="abs rating-name" style="left:500px; width:216px; text-align:center; top:1784px">Ratewell</div>

    <div class="rating" style="top:1840px">Excellent</div>
    <svg class="stars" style="top:1836px" width="180" height="34" viewBox="0 0 216 42" aria-hidden="true">
      <g fill="var(--star)">
        <use href="#star"/><use href="#star" x="43"/><use href="#star" x="86"/><use href="#star" x="129"/><use href="#star" x="172"/>
      </g>
    </svg>
    <div class="abs rating-name" style="left:470px; width:240px; text-align:center; top:1880px; font-size:22px">Praisly Reviews</div>
  </section>
  <div class="rule" style="top:1972px"></div>

  <section class="mailing">
    <div class="mailing-title">Sign up to our mailing list</div>
    <p class="mailing-text">For event invitations, exclusive previews,<br>latest stock + special offers</p>
    <div class="mailing-form">
      <div class="mailing-input">Email ...</div>
      <div class="mailing-button">SUBSCRIBE</div>
    </div>
  </section>
  <div class="rule" style="top:2380px"></div>

  <section>
    <h2 class="abs center heading" style="top:2478px">Contact Us</h2>
    <div class="abs brand-name" style="left:268px; top:2628px; width:250px; text-align:center; line-height:40px">Velmor<br><span style="font-size:18px; letter-spacing:4px">Car House</span></div>
    <svg class="abs" style="left:532px; top:2600px" width="24" height="32" viewBox="0 0 24 32" aria-hidden="true">
      <path d="M12 1C6 1 1.5 5.5 1.5 11.3 1.5 19 12 31 12 31s10.5-12 10.5-19.7C22.5 5.5 18 1 12 1z" fill="var(--ink)"/>
      <circle cx="12" cy="11" r="4" fill="var(--bg-deep)"/>
    </svg>
    <div class="address" style="top:2594px">Hollins Road (A412),<br>Kestley,<br>Surrey KT9 4QL</div>
  </section>
  <div class="rule" style="top:2788px"></div>

  <section>
    <h2 class="abs center heading" style="top:2854px">Partners</h2>
    <div class="partner" style="left:290px">Calderon Bank</div>
    <div class="partner" style="left:700px">Quorin Finance</div>
  </section>
  <div class="rule" style="top:3120px"></div>

  <section>
    <h2 class="abs center heading heading--caps" style="top:3190px">Follow Us</h2>
    <div class="social-label" style="left:208px">Circlebook</div>
    <div class="social-label" style="left:404px">Chirper</div>
    <div class="social-label" style="left:596px">Snapframe</div>
    <div class="social-label" style="left:812px">Viewtube</div>
    <div class="social-label" style="left:1000px">Workline</div>
    <div class="social-tile" style="left:208px">CB</div>
    <div class="social-tile" style="left:404px">CH</div>
    <div class="social-tile" style="left:596px">SF</div>
    <div class="social-tile" style="left:812px">VT</div>
    <div class="social-tile" style="left:1000px">WL</div>
  </section>
  <div class="rule" style="top:3540px"></div>

  <footer>
    <div class="abs center legal" style="top:3618px">Cookie Policy | Sitemap</div>
    <div class="abs center legal" style="top:3688px">©Copyright information here</div>
  </footer>
</body>
</html>
```